Garden Design Flier

I would like a PDF of this half page A4 flier in soft green tones with dark green leaves.

Target Market(s)

Home owners and real estate agents

Font styles to use
Serif
Other font styles liked:
• Papyrus

Colors
acd136
9bcb3c
cadf82
fefdec

Requirements
Must have
• Green tones
Nice to have
• Leaves, vines, lawns
Should not have
• Open to ideas, but classic style

```html
<!DOCTYPE html>
<html lang="en">
<head>
<meta charset="utf-8">
<title>Verdant Gardens – Garden Design Flier</title>
<link rel="stylesheet" href="https://fonts.googleapis.com/css2?family=Roboto+Slab:wght@300;400;600;800&display=swap">
<style>
  :root {
    --mint: #acd9b9;
    --mint-soft: #c6e6cf;
    --leaf-dark: #3a5a4a;
    --leaf-mid: #8fc2a0;
    --paper: #ffffff;
    --ink: #111111;
  }
  * { margin: 0; padding: 0; box-sizing: border-box; }
  html, body { width: 1200px; height: 849px; overflow: hidden; background: var(--mint); }
  .flier {
    position: relative;
    width: 1200px;
    height: 849px;
    background: var(--mint);
    font-family: "Roboto Slab", Georgia, serif;
    overflow: hidden;
  }
  .flier__panel {
    position: absolute;
    left: 56px; top: 56px;
    width: 1087px; height: 735px;
    background: var(--paper);
  }
  .foliage { position: absolute; }
  .foliage--top-left {
    left: -20px; top: -20px; width: 287px; height: 300px;
    background: var(--leaf-dark);
    border-radius: 30% 60% 55% 45% / 35% 45% 60% 55%;
  }
  .foliage--top-right {
    left: 930px; top: -10px; width: 280px; height: 292px;
    background: var(--leaf-mid);
    border-radius: 55% 30% 45% 60% / 45% 35% 55% 50%;
  }
  .foliage--left-sprig {
    left: -10px; top: 360px; width: 164px; height: 230px;
    background: var(--mint-soft);
    border-radius: 20% 70% 70% 20% / 30% 50% 50% 30%;
  }
  .foliage--bottom-left {
    left: -10px; top: 674px; width: 227px; height: 185px;
    background: var(--leaf-mid);
    border-radius: 20% 80% 30% 40% / 30% 70% 30% 60%;
  }
  .foliage--bottom-right {
    left: 1027px; top: 601px; width: 183px; height: 212px;
    background: var(--leaf-dark);
    border-radius: 50% 30% 40% 55% / 40% 30% 55% 45%;
  }
  .brand {
    position: absolute;
    left: 0; right: 0; top: 96px;
    text-align: center;
    color: var(--leaf-dark);
    font-weight: 800;
  }
  .brand__main {
    display: block;
    font-size: 78px;
    line-height: 78px;
    letter-spacing: 0.42em;
    padding-left: 0.42em;
  }
  .brand__sub {
    display: block;
    margin-top: 10px;
    font-size: 46px;
    line-height: 48px;
    letter-spacing: 0.5em;
    padding-left: 0.5em;
  }
  .byline {
    position: absolute;
    left: 0; right: 0; top: 236px;
    display: flex;
    justify-content: center;
    align-items: center;
    gap: 10px;
    font-size: 25px;
    font-weight: 400;
    color: var(--ink);
    letter-spacing: 0.02em;
  }
  .byline__sprig {
    width: 12px; height: 28px;
    background: var(--leaf-dark);
    border-radius: 50%;
  }
  .credential {
    position: absolute;
    left: 351px; top: 294px;
    width: 498px; height: 51px;
    border-radius: 26px;
    background: var(--leaf-dark);
    color: #fff;
    font-size: 19px;
    font-weight: 600;
    letter-spacing: 0.06em;
    display: flex;
    align-items: center;
    justify-content: center;
    gap: 12px;
  }
  .services {
    position: absolute;
    left: 240px; width: 720px; top: 370px;
    display: flex;
    justify-content: space-between;
    list-style: none;
    font-size: 44px;
    font-weight: 400;
    color: var(--ink);
    letter-spacing: 0.02em;
  }
  .laurel {
    position: absolute;
    top: 455px; width: 81px; height: 175px;
    background: var(--leaf-dark);
  }
  .laurel--left { left: 222px; border-radius: 100% 0 0 100% / 50% 0 0 50%; clip-path: polygon(40% 0, 60% 0, 20% 50%, 80% 100%, 55% 100%, 0 50%); }
  .laurel--right { left: 896px; clip-path: polygon(40% 0, 60% 0, 100% 50%, 45% 100%, 20% 100%, 80% 50%); }
  .pitch {
    position: absolute;
    left: 270px; width: 660px; top: 494px;
    text-align: center;
    font-size: 23px;
    line-height: 32.5px;
    font-weight: 300;
    color: var(--ink);
  }
  .contact {
    position: absolute;
    left: 0; right: 0; top: 676px;
    text-align: center;
    list-style: none;
    font-size: 22px;
    line-height: 32px;
    font-weight: 400;
    color: var(--leaf-dark);
    letter-spacing: 0.03em;
  }
</style>
</head>
<body>
<main class="flier">
  <div class="flier__panel"></div>

  <div class="foliage foliage--top-left" role="img" aria-label="Dark green monstera leaf illustration"></div>
  <div class="foliage foliage--top-right" role="img" aria-label="Outlined monstera leaf illustration"></div>
  <div class="foliage foliage--left-sprig" role="img" aria-label="Pale green leafy sprig illustration"></div>
  <div class="foliage foliage--bottom-left" role="img" aria-label="Outlined olive sprig illustration"></div>
  <div class="foliage foliage--bottom-right" role="img" aria-label="Dark green monstera leaf illustration"></div>

  <h1 class="brand">
    <span class="brand__main">VERDANT</span>
    <span class="brand__sub">GARDENS</span>
  </h1>

  <p class="byline">
    <span class="byline__sprig" role="img" aria-label="Small leaf ornament"></span>
    <span>by Liam Hartley</span>
    <span class="byline__sprig" role="img" aria-label="Small leaf ornament"></span>
  </p>

  <p class="credential">
    <span>Certificate 3</span><span>|</span><span>Horticulture</span><span>|</span><span>Vale Institute</span>
  </p>

  <ul class="services">
    <li>Design</li>
    <li>Install</li>
    <li>Grow</li>
    <li>Tend</li>
    <li>Enjoy</li>
  </ul>

  <div class="laurel laurel--left" role="img" aria-label="Laurel branch ornament"></div>
  <div class="laurel laurel--right" role="img" aria-label="Laurel branch ornament"></div>

  <p class="pitch">All your gardening and landscaping needs from design and installation to general maintenance Bespoke vegetable gardens and potager designs created to suite your site and requirements</p>

  <ul class="contact">
    <li>Email: liam@verdantgardens.com.au</li>
    <li>Mobile: 0400-123456</li>
    <li>ABN: 12345678901</li>
  </ul>
</main>
</body>
</html>
```